4D Hush Little Nest Luxury Ultrasound Billboard

Design a HIGH-END, MODERN billboard for my private prenatal ultrasound studio, 4D Hush Little Nest, located in Pace, Florida.
This billboard will be viewed by drivers traveling at highway speeds, so it must be extremely clean, simple, and readable within 6 seconds.
About My Business
4D Hush Little Nest is a private prenatal ultrasound studio specializing in:
Highest technology 4D/HD Ultrasounds
Early Gender Determination
Pregnancy Confirmation
I have been serving families for nearly 10 years and is known for creating a memorable experience, not just an ultrasound appointment.
Design Style
I DO NOT want:
Flowers
Leaves
Swirls
Glitter
Hearts everywhere
Busy backgrounds
Generic maternity stock graphics
I DO want:
Modern
Luxury
Upscale
Clean
Professional
Eye-catching
Premium medical spa feel
Colors
Use colors from my logo:
LOGO Green ( or a deep green)
Black
White
Soft Gold accents
Images:
Incorporate my professional headshot in a clean, modern way, logo, and the ultrasound images
Text
Keep wording minimal.
Primary Headline ( OPEN TO IDEAS) :
EXAMPLES ( WOULD RATHER SOMETHING MORE CATCHY)
" ADVANCED IMAGING. UNFORGETTABLE MOMENTS"
"MEET YOUR BABY BEFORE BIRTH"
Under headline:
4D Ultrasound • Early Gender • Pregnancy Confirmation
Business Name:
4D Hush Little Nest
Private Prenatal Ultrasound Studio
Phone Number:
850-471-3905
Important
This billboard must be readable in 5–6 seconds from a moving vehicle.
Less text is better.
The phone number and business name must be visible from a distance.
The design should feel like a premium brand that immediately tells expecting parents:
“This is where I go to see my baby.”
Files Provided
Official logo
Headshot
Ultrasound images
Don’t make this look like a medical office billboard.
Make it look like a luxury baby experience billboard. That’s what separates 4D Hush Little Nest from hospitals, OB offices, and all the new studios popping up around you. The emotional connection is what gets moms to book. ❤️
Billboard Size - 10.6” x 36”

```html
<!DOCTYPE html>
<html lang="en">
<head>
<meta charset="utf-8">
<title>4D Hush Little Nest — Billboard</title>
<link rel="stylesheet" href="https://fonts.googleapis.com/css2?family=Playfair+Display:wght@700;800&family=Poppins:wght@500;600&display=swap">
<style>
  :root {
    --gold: #c9a235;
    --gold-pale: #f1e0ad;
    --gold-light: #f7ecc9;
    --sage: #86a08e;
    --deep-green: #4f6a5c;
    --slate: #5b6660;
    --cream: #f7f0e4;
    --white: #ffffff;
    --skin: #d9a98a;
    --hair: #c9a878;
    --cloth: #ebe4da;
  }
  * { margin: 0; padding: 0; box-sizing: border-box; }
  html, body { width: 1200px; height: 352px; overflow: hidden; background: var(--white); }
  .billboard {
    position: relative;
    width: 1200px;
    height: 352px;
    overflow: hidden;
    background: linear-gradient(135deg, var(--gold-light), var(--gold-pale) 55%, var(--gold-light));
  }
  .photo { position: absolute; top: 0; height: 352px; }
  .photo--headshot {
    left: 0; width: 236px;
    background: radial-gradient(ellipse at 55% 35%, var(--skin) 0%, #c99a7c 30%, var(--hair) 60%, #9c8260 100%);
  }
  .photo--expecting {
    left: 236px; width: 300px;
    background: linear-gradient(90deg, #f3eee8 0%, var(--cloth) 20%, var(--skin) 45%, #d4a283 65%, var(--cloth) 85%, #efe9e1 100%);
  }
  .brand-card {
    position: absolute;
    left: 28px; top: 191px;
    width: 254px; height: 142px;
    background: var(--white);
    border-radius: 12px;
    padding: 6px;
  }
  .brand-card__frame {
    width: 100%; height: 100%;
    border: 2px solid var(--deep-green);
    border-radius: 10px;
    display: flex;
    flex-direction: column;
    align-items: center;
    justify-content: center;
    padding: 8px 10px 8px;
  }
  .brand-card__name {
    font-family: "Playfair Display", Georgia, serif;
    font-weight: 700;
    font-size: 31px;
    line-height: 1.02;
    color: var(--deep-green);
    text-align: center;
  }
  .brand-card__name span { display: block; }
  .brand-card__rule {
    width: 212px;
    height: 1px;
    background: var(--gold);
    margin: 9px 0 7px;
  }
  .brand-card__tagline {
    font-family: "Poppins", Arial, sans-serif;
    font-weight: 500;
    font-size: 10px;
    letter-spacing: 0.4px;
    color: var(--slate);
    text-transform: uppercase;
    white-space: nowrap;
  }
  .message { position: absolute; left: 531px; top: 0; width: 669px; height: 352px; }
  .message text { fill: var(--cream); }
  .headline { font-family: "Playfair Display", Georgia, serif; font-weight: 700; }
  .services { font-family: "Poppins", Arial, sans-serif; font-weight: 600; }
  .phone {
    font-family: "Playfair Display", Georgia, serif;
    font-weight: 700;
    font-variant-numeric: lining-nums;
    font-feature-settings: "lnum" 1;
  }
</style>
</head>
<body>
<main class="billboard">
  <div class="photo photo--headshot" role="img" aria-label="Professional headshot of the studio owner, smiling, with long wavy blonde hair"></div>
  <div class="photo photo--expecting" role="img" aria-label="Expecting mother in cream loungewear showing her bump while holding a strip of ultrasound prints"></div>

  <div class="brand-card">
    <div class="brand-card__frame">
      <p class="brand-card__name"><span>4D Hush</span><span>Little Nest</span></p>
      <span class="brand-card__rule"></span>
      <p class="brand-card__tagline">Prenatal Ultrasound Studio</p>
    </div>
  </div>

  <svg class="message" viewBox="0 0 669 352" width="669" height="352" aria-label="Meet your baby before birth. 4D Ultrasound, Early Gender, Pregnancy Confirmation. 850-471-3905">
    <rect class="band band--gold" x="5" y="37" width="664" height="184" fill="var(--gold)"/>
    <rect class="band band--green" x="0" y="221" width="669" height="100" fill="var(--sage)"/>
    <text class="headline" x="54" y="102" font-size="64" textLength="566" lengthAdjust="spacingAndGlyphs">MEET YOUR BABY</text>
    <text class="headline" x="50" y="172" font-size="72" textLength="570" lengthAdjust="spacingAndGlyphs">BEFORE BIRTH</text>
    <text class="services" x="54" y="204" font-size="19" textLength="566" lengthAdjust="spacingAndGlyphs">4D Ultrasound • Early Gender • Pregnancy Confirmation</text>
    <text class="phone" x="49" y="303" font-size="86" textLength="569" lengthAdjust="spacingAndGlyphs">850-471-3905</text>
  </svg>
</main>
</body>
</html>
```